Brevin Law Client Handbook

We are a small, rapidly growing, criminal defense law firm located in a suburb of Seattle, WA. The cover should be professional and be consistent with our image a sleek, modern, and efficient. The included files show our designs used in other projects for reference.

```html
<!DOCTYPE html>
<html lang="en">
<head>
<meta charset="utf-8">
<title>Brevin Law Firm — Client Handbook Cover</title>
<link href="https://fonts.googleapis.com/css2?family=Cinzel:wght@400&family=Source+Sans+3:wght@400&display=swap" rel="stylesheet">
<style>
  :root {
    --backdrop: #7890a0;
    --navy: #0f3557;
    --navy-soft: #163d62;
    --white: #ffffff;
  }
  * { margin: 0; padding: 0; box-sizing: border-box; }
  html, body { width: 1200px; height: 857px; overflow: hidden; }
  body { background: var(--backdrop); position: relative; font-family: "Cinzel", serif; color: var(--white); }

  .cover, .spine {
    position: absolute;
    top: 118px;
    height: 617px;
    background: var(--navy);
  }
  .cover--back  { left: 89px;  width: 421px; }
  .spine        { left: 563px; width: 69px; }
  .cover--front { left: 677px; width: 421px; }

  .cover__pattern {
    position: absolute; inset: 0;
    background: linear-gradient(180deg, var(--navy-soft), var(--navy));
  }

  .label-band {
    position: absolute;
    top: 282px;
    height: 56px;
    width: 189px;
    background: var(--white);
  }
  .cover--back .label-band  { right: 0; }
  .cover--front .label-band { left: 0; }

  .wordmark {
    position: absolute;
    top: 284px;
    display: flex;
    align-items: flex-start;
    gap: 14px;
  }
  .cover--back .wordmark  { left: 63px; }
  .cover--front .wordmark { left: 210px; }

  .wordmark__square {
    width: 28px; height: 28px;
    margin-top: 1px;
    background: var(--white);
  }
  .wordmark__text { text-align: center; line-height: 1; }
  .wordmark__name {
    display: block;
    font-size: 23px;
    letter-spacing: 0.22em;
    margin-right: -0.22em;
  }
  .wordmark__sub {
    display: block;
    font-size: 10px;
    letter-spacing: 0.18em;
    margin-top: 5px;
  }
  .edition {
    display: block;
    font-size: 9.5px;
    letter-spacing: 0.02em;
    margin-top: 14px;
    white-space: nowrap;
  }

  .contact {
    position: absolute;
    left: 81px;
    top: 476px;
    font-family: "Source Sans 3", sans-serif;
    font-size: 6.6px;
    line-height: 9px;
    font-style: normal;
  }
  .contact__web { margin-top: 9px; display: block; }

  .spine__square {
    position: absolute;
    left: 20px; top: 97px;
    width: 30px; height: 24px;
    background: var(--white);
  }
  .spine__name, .spine__title {
    position: absolute;
    left: 50%;
    transform: translateX(-50%);
    writing-mode: vertical-rl;
    white-space: nowrap;
  }
  .spine__name {
    top: 134px;
    font-size: 19px;
    letter-spacing: 0.24em;
  }
  .spine__title {
    top: 286px;
    font-size: 17px;
    letter-spacing: 0.02em;
  }
</style>
</head>
<body>
  <section class="cover cover--back">
    <div class="cover__pattern" role="img" aria-label="Faint repeating firm name pattern across the navy cover"></div>
    <div class="wordmark">
      <span class="wordmark__square"></span>
      <div class="wordmark__text">
        <span class="wordmark__name">BREVIN</span>
        <span class="wordmark__sub">LAW FIRM</span>
        <span class="edition">FOR LAW ENFORCEMENT</span>
      </div>
    </div>
    <address class="contact">
      1820 Harbor Point Dr NE<br>
      Suite 210<br>
      Kirkland, WA 98034
      <span class="contact__web">www.brevinlawfirm.com</span>
    </address>
    <div class="label-band"></div>
  </section>

  <section class="spine">
    <span class="spine__square"></span>
    <span class="spine__name">BREVIN</span>
    <span class="spine__title">FOR LAW ENFORCEMENT</span>
  </section>

  <section class="cover cover--front">
    <div class="cover__pattern" role="img" aria-label="Faint repeating firm name pattern across the navy cover"></div>
    <div class="label-band"></div>
    <div class="wordmark">
      <span class="wordmark__square"></span>
      <div class="wordmark__text">
        <span class="wordmark__name">BREVIN</span>
        <span class="wordmark__sub">LAW FIRM</span>
        <span class="edition">FOR LAW ENFORCEMENT</span>
      </div>
    </div>
  </section>
</body>
</html>
```